" O Instituto Raiz Clara tem como alicerce o fortalecimento e empoderamento do movimento que gere autonomia para a vida Consolidada há 20 anos num modelo de atuação multidisciplinar que desenvolve estratégias voltadas a promoção de uma vida sustentável e funcional. Nesse sentido consolidamos um trabalho junto a população menos favorecida e em vulnerabilidade social buscando estratégias de impacto nos eixos de atividade física, educação, cultura e lazer que capacitem o protagonismo de suas vidas. Para tanto atuamos com planejamento estratégico e ações práticas voltados a seguinte demanda: 1. Combate a Obesidade Infato Juvenil 2. Programa voltado a dependentes quimicos 3. Combate ao sedentarismo e obesidade 4. Programa voltado ao Envelhecimento Sustentável 5. Programa de inclusão através de atividades artisticas Entre outros "

```html
<!DOCTYPE html>
<html lang="pt-BR">
<head>
<meta charset="UTF-8">
<title>Papel Timbrado — Instituto Raiz Clara</title>
<link href="https://fonts.googleapis.com/css2?family=Montserrat:wght@400;600;700&display=swap" rel="stylesheet">
<style>
  :root {
    --backdrop: #e9ebec;
    --paper: #ffffff;
    --brand-teal: #2f8fb0;
    --band-top: #8dbfca;
    --band-bottom: #5e9cae;
    --band-text: #ffffff;
    --accent-lavender: #d9d4e6;
    --accent-green: #e3eed6;
  }
  * { margin: 0; padding: 0; box-sizing: border-box; }
  html, body {
    width: 1200px;
    height: 1200px;
    overflow: hidden;
  }
  body {
    background: var(--backdrop);
    font-family: "Montserrat", sans-serif;
    display: flex;
    align-items: center;
    justify-content: center;
  }
  .letterhead {
    position: relative;
    width: 760px;
    height: 1075px;
    background: var(--paper);
    box-shadow: 0 6px 24px rgba(0, 0, 0, 0.12);
    overflow: hidden;
  }
  .letterhead__brand {
    position: absolute;
    top: 70px;
    left: 78px;
    display: flex;
    align-items: center;
    gap: 12px;
  }
  .brand__dot {
    width: 30px;
    height: 30px;
    border-radius: 50%;
    background: var(--brand-teal);
  }
  .brand__name {
    color: var(--brand-teal);
    font-weight: 700;
    font-size: 19px;
    letter-spacing: 0.02em;
  }
  .letterhead__decor {
    position: absolute;
    inset: 0;
    width: 100%;
    height: 100%;
  }
  .letterhead__footer {
    position: absolute;
    left: 0;
    right: 0;
    bottom: 0;
    height: 150px;
  }
  .footer__band {
    position: absolute;
    inset: 0;
    width: 100%;
    height: 100%;
  }
  .footer__content {
    position: absolute;
    left: 0;
    right: 0;
    top: 64px;
    text-align: center;
    color: var(--band-text);
  }
  .footer__tagline {
    font-weight: 700;
    font-size: 17px;
    margin-bottom: 12px;
  }
  .footer__social {
    display: inline-flex;
    align-items: center;
    gap: 8px;
    font-size: 12px;
    font-weight: 400;
  }
  .social__dot {
    width: 14px;
    height: 14px;
    border-radius: 50%;
    background: var(--band-text);
    opacity: 0.9;
  }
</style>
</head>
<body>
  <main class="letterhead">
    <svg class="letterhead__decor" viewBox="0 0 760 1075" role="img" aria-label="Faint decorative figures in lavender and green">
      <defs>
        <radialGradient id="decor-lavender" cx="50%" cy="50%" r="50%">
          <stop offset="0%" stop-color="var(--accent-lavender)" stop-opacity="0.9"/>
          <stop offset="100%" stop-color="var(--accent-lavender)" stop-opacity="0"/>
        </radialGradient>
        <radialGradient id="decor-green" cx="50%" cy="50%" r="50%">
          <stop offset="0%" stop-color="var(--accent-green)" stop-opacity="0.9"/>
          <stop offset="100%" stop-color="var(--accent-green)" stop-opacity="0"/>
        </radialGradient>
      </defs>
      <ellipse cx="620" cy="790" rx="190" ry="260" fill="url(#decor-lavender)"/>
      <ellipse cx="320" cy="820" rx="170" ry="130" fill="url(#decor-green)"/>
    </svg>

    <header class="letterhead__brand">
      <span class="brand__dot"></span>
      <span class="brand__name">Instituto Raiz Clara</span>
    </header>

    <footer class="letterhead__footer">
      <svg class="footer__band" viewBox="0 0 760 150" preserveAspectRatio="none" aria-hidden="true">
        <defs>
          <linearGradient id="band-fill" x1="0" y1="0" x2="0" y2="1">
            <stop offset="0%" stop-color="var(--band-top)"/>
            <stop offset="100%" stop-color="var(--band-bottom)"/>
          </linearGradient>
        </defs>
        <path d="M0 40 Q380 -10 760 40 L760 150 L0 150 Z" fill="url(#band-fill)"/>
      </svg>
      <div class="footer__content">
        <p class="footer__tagline">Fortalecendo Raízes!</p>
        <p class="footer__social"><span class="social__dot"></span>@institutoraizclara</p>
      </div>
    </footer>
  </main>
</body>
</html>
```